Brisa Vale residential and commercial cleaning

We need a Business card design for a new residential and commercial cleaning company based in UAE- Abu Dhabi named (BRISA VALE)
we provide a residential cleaning service based in hourly rate (Maid Rent - Baby Setting), Also a commercial and offices cleaning.
Our logo is attached for your reference

Target Market(s)

Women who are 22 to 60 years old.

Industry/Entity Type

Residential

Requirements
Should not have
• it should not have an old-style fonts

```html
<!DOCTYPE html>
<html lang="en">
<head>
<meta charset="utf-8">
<title>Brisa Vale Business Card</title>
<link href="https://fonts.googleapis.com/css2?family=Open+Sans:wght@400;600;700&display=swap" rel="stylesheet">
<style>
  :root {
    --backdrop: #ecebe8;
    --card-white: #ffffff;
    --brand-blue: #2f8bbf;
    --brand-deep-blue: #1d6fae;
    --leaf-green: #a6cf38;
    --text-light: #ffffff;
  }
  * { box-sizing: border-box; margin: 0; padding: 0; }
  html, body {
    width: 1200px; height: 900px; overflow: hidden;
    background: var(--backdrop);
    font-family: "Open Sans", sans-serif;
  }
  .business-card {
    position: absolute; left: 390px; top: 130px;
    width: 420px; height: 640px;
    background: var(--card-white);
    border-radius: 34px 34px 0 0;
    overflow: hidden;
    box-shadow: 0 6px 22px rgba(0,0,0,0.15);
  }
  .card-shapes { position: absolute; inset: 0; }
  .brand-lockup {
    position: absolute; left: 44px; top: 92px;
    display: flex; align-items: center; gap: 16px;
  }
  .brand-name {
    font-size: 46px; font-weight: 700; color: var(--brand-deep-blue);
    letter-spacing: -1px; line-height: 1;
  }
  .brand-circle {
    width: 78px; height: 78px; border-radius: 50%;
    border: 4px solid var(--leaf-green);
  }
  .holder {
    position: absolute; left: 0; right: 0; top: 365px;
    text-align: center; color: var(--text-light);
  }
  .holder-name { font-size: 24px; font-weight: 400; letter-spacing: 0.5px; line-height: 1.1; }
  .holder-title { font-size: 13px; font-weight: 600; letter-spacing: 0.5px; }
  .contact-list {
    position: absolute; left: 0; right: 0; top: 452px;
    list-style: none; text-align: center; color: var(--text-light);
  }
  .contact-item { margin-bottom: 7px; font-size: 14px; line-height: 1.3; }
  .contact-icon {
    display: block; margin: 0 auto 3px;
    width: 18px; height: 18px; border-radius: 3px;
    background: var(--card-white);
  }
</style>
</head>
<body>
  <div class="business-card">
    <svg class="card-shapes" viewBox="0 0 420 640" width="420" height="640" aria-hidden="true">
      <path fill="var(--leaf-green)" d="M0,330 C0,270 30,255 80,248 L350,205 C400,198 420,215 420,245 L420,640 L0,640 Z"/>
      <path fill="var(--brand-blue)" d="M0,370 C0,300 30,285 85,276 L355,232 C405,225 420,242 420,272 L420,640 L0,640 Z"/>
    </svg>

    <div class="brand-lockup">
      <span class="brand-name">Brisa Vale</span>
      <span class="brand-circle"></span>
    </div>

    <div class="holder">
      <p class="holder-name">YOUR NAME</p>
      <p class="holder-title">DIRECTOR</p>
    </div>

    <ul class="contact-list">
      <li class="contact-item">
        <svg class="contact-icon" viewBox="0 0 18 18"><rect width="18" height="18" rx="3" fill="#fff"/><path d="M9 3.5a3.6 3.6 0 0 0-3.6 3.6C5.4 10 9 14.5 9 14.5s3.6-4.5 3.6-7.4A3.6 3.6 0 0 0 9 3.5zm0 5a1.4 1.4 0 1 1 0-2.8 1.4 1.4 0 0 1 0 2.8z" fill="var(--brand-blue)"/></svg>
        14 Corniche Road, Al Khalidiya, Abu Dhabi
      </li>
      <li class="contact-item">
        <svg class="contact-icon" viewBox="0 0 18 18"><rect width="18" height="18" rx="3" fill="#fff"/><path d="M6 3.5l2 3-1.2 1.2a7 7 0 0 0 3.5 3.5L11.5 10l3 2-1 2.2C8.5 14.5 3.5 9.5 3.8 4.5z" fill="var(--brand-blue)"/></svg>
        +971-25550147
      </li>
      <li class="contact-item">
        <svg class="contact-icon" viewBox="0 0 18 18"><rect width="18" height="18" rx="3" fill="#fff"/><rect x="3.5" y="5" width="11" height="8" rx="1" fill="none" stroke="var(--brand-blue)" stroke-width="1.4"/><path d="M3.8 5.5L9 9.5l5.2-4" fill="none" stroke="var(--brand-blue)" stroke-width="1.4"/></svg>
        hello@brisavale.com
      </li>
      <li class="contact-item">
        <svg class="contact-icon" viewBox="0 0 18 18"><rect width="18" height="18" rx="3" fill="#fff"/><circle cx="9" cy="9" r="5.3" fill="none" stroke="var(--brand-blue)" stroke-width="1.3"/><path d="M3.7 9h10.6M9 3.7c-2.4 2.8-2.4 7.8 0 10.6M9 3.7c2.4 2.8 2.4 7.8 0 10.6" fill="none" stroke="var(--brand-blue)" stroke-width="1.1"/></svg>
        www.brisavale.com
      </li>
    </ul>
  </div>
</body>
</html>
```